Doctors clinic requires stationary designed

We require various types of stationary to be design based on the logo (attached). We require the following:
- Letterhead (A4 Portrait)
- Business Card (must include UV spot on rear)
- With compliments slip (DL Landscape)
- Appointments card (Folded A6)

We are a young clinical practice which boasts a modern and sophisticated approach to medicine so we require something which feels fresh and modern. Please include colours represented in the logo (contrasting teal and grey). We are calling for creative minds to put forth their ideas and we will be actively providing feedback on all designs.

thank you

```html
<!DOCTYPE html>
<html lang="en">
<head>
<meta charset="utf-8">
<title>Dr Clara Holloway – Business Card</title>
<link href="https://fonts.googleapis.com/css2?family=Open+Sans:wght@400;600;700&display=swap" rel="stylesheet">
<style>
  :root{
    --teal:#1a8c80;
    --teal-dark:#137368;
    --grey:#9a9a9a;
    --grey-light:#c9c9ca;
    --ink:#1e1e1e;
    --paper:#ffffff;
    --backdrop:#2a2a2a;
  }
  *{box-sizing:border-box;margin:0;padding:0}
  html,body{width:1200px;height:871px;overflow:hidden}
  body{
    background:var(--backdrop);
    font-family:"Open Sans",Arial,sans-serif;
    display:flex;align-items:center;justify-content:center;gap:40px;
  }
  .card{
    position:relative;width:560px;height:320px;overflow:hidden;
    background:var(--paper);
    box-shadow:0 10px 30px rgba(0,0,0,.5);
  }
  /* rear */
  .card--back{
    background:linear-gradient(135deg,#ffffff 0%,#e2e2e2 45%,#f4f4f4 70%,#d6d6d6 100%);
    display:flex;align-items:center;justify-content:center;
  }
  .brand{display:flex;align-items:center;gap:14px}
  .brand__mark{width:58px;height:58px;border:3px solid var(--teal);border-radius:50%;flex:none}
  .brand__name{color:var(--teal);font-weight:700;font-size:24px;line-height:1.1}
  .brand__tagline{color:var(--grey);font-weight:600;font-size:13px;margin-top:2px}
  /* front */
  .card--front .brand{position:absolute;left:36px;top:34px}
  .holder{position:absolute;left:40px;top:140px}
  .holder__name{font-weight:700;font-size:15px;letter-spacing:3px;color:var(--ink)}
  .holder__role{font-size:10px;letter-spacing:1.5px;color:var(--teal);margin-top:4px}
  .rule{position:absolute;left:40px;right:40px;top:186px;height:1px;background:var(--grey-light)}
  .contacts{position:absolute;left:40px;top:198px;list-style:none}
  .contacts li{display:flex;align-items:center;gap:12px;font-size:10.5px;letter-spacing:1px;color:#444;height:18px}
  .contacts svg{width:12px;height:12px;fill:none;stroke:var(--teal);stroke-width:1.4}
  .address{position:absolute;right:40px;top:214px;text-align:right;font-size:10px;letter-spacing:1.5px;line-height:1.65;color:var(--grey)}
  .band-grey{position:absolute;left:0;bottom:0;width:100%;height:36px;background:var(--grey-light)}
  .band-teal{
    position:absolute;right:0;bottom:0;width:300px;height:36px;
    background:var(--teal);border-top-left-radius:22px;
    box-shadow:-4px 0 0 var(--paper);
    display:flex;align-items:center;justify-content:flex-end;padding-right:40px;
    color:#fff;font-size:11.5px;font-weight:600;letter-spacing:2px;
  }
</style>
</head>
<body>
  <section class="card card--back" aria-label="Card rear">
    <div class="brand">
      <span class="brand__mark"></span>
      <div>
        <div class="brand__name">Dr Clara Holloway</div>
        <div class="brand__tagline">Obstetrician and Gynaecologist</div>
      </div>
    </div>
  </section>

  <section class="card card--front" aria-label="Card front">
    <div class="brand">
      <span class="brand__mark"></span>
      <div>
        <div class="brand__name">Dr Clara Holloway</div>
        <div class="brand__tagline">Obstetrician and Gynaecologist</div>
      </div>
    </div>

    <div class="holder">
      <div class="holder__name">Dr. Clara Holloway</div>
      <div class="holder__role">Doctor</div>
    </div>

    <div class="rule"></div>

    <ul class="contacts">
      <li>
        <svg viewBox="0 0 12 12" aria-hidden="true"><path d="M2 4.5 Q6 1 10 4.5 L9 6 L7.5 5 L7.5 4 Q6 3.5 4.5 4 L4.5 5 L3 6 Z M3 7 H9 V10 H3 Z"/></svg>
        9512 3864
      </li>
      <li>
        <svg viewBox="0 0 12 12" aria-hidden="true"><rect x="1.5" y="3" width="9" height="6.5"/><path d="M1.5 3 L6 7 L10.5 3"/></svg>
        9512 3865
      </li>
      <li>
        <svg viewBox="0 0 12 12" aria-hidden="true"><circle cx="6" cy="6" r="4.5"/><path d="M1.5 6 H10.5 M6 1.5 Q3.5 6 6 10.5 M6 1.5 Q8.5 6 6 10.5"/></svg>
        clara@drclaraholloway.com.au
      </li>
    </ul>

    <address class="address" style="font-style:normal">
      Westmere Private Hospital<br>
      Suite 12 Spec. Med. Centre (West)<br>
      Harbour Ave, Westmere
    </address>

    <div class="band-grey"></div>
    <div class="band-teal">web: drclaraholloway.com.au</div>
  </section>
</body>
</html>
```